Website page design

Hi, I need to improve the look of my homepage and the final offer page of my website. www.Pebble7dock.com We have an orvex buyback program where we purchase used orvex products from consumers nationwide. If you would go click through a sample offer on the site, you will the last view final offer page where we give you a cash offer for you site. I would like to keep the red and white colors since my logo is red and white. Please pay attention to the information shown on the homepage now, it is important for me to show the visitors this information on the home page. I would also love to give the users a friendly and inviting look when clicking on the options of orvex products on the home page.

Target Market(s)

Orvex electronics consumers

Number of Pages Required

2 page

Requirements
Nice to have
• On the final offer page, i would love for the offer to give an exciting look for the pebble 7 dock offer, and a boring look for the orvex buy back offer. At the final offer page you will my websites offer ( Your Pebble7dock Offer ) vs ( Orvex buyback program offer ) which is my competitor.

```html
<!DOCTYPE html>
<html lang="en">
<head>
<meta charset="utf-8">
<title>Pebble7dock — Sell Your Orvex Device</title>
<link href="https://fonts.googleapis.com/css2?family=Questrial&family=Poppins:wght@600;700&family=Open+Sans:wght@400;600&display=swap" rel="stylesheet">
<style>
:root{
  --red:#c30a1c;
  --red-deep:#8e0612;
  --red-dark:#6d0410;
  --ink:#2a2a2a;
  --muted:#555;
  --frame:#e3e3e3;
  --white:#fff;
  --font-light:"Questrial",sans-serif;
  --font-bold:"Poppins",sans-serif;
  --font-body:"Open Sans",sans-serif;
}
*{box-sizing:border-box;margin:0;padding:0}
html,body{width:1200px;height:2896px;overflow:hidden;background:var(--white)}
body{position:relative;font-family:var(--font-body);color:var(--ink)}
.abs{position:absolute}
.hero-photo{left:0;top:0;width:1200px;height:706px;background:linear-gradient(120deg,#d9d4cf 0%,#bfb6ac 40%,#e8e3de 75%,#f2efec 100%)}
.laptop-area{left:120px;top:260px;width:480px;height:380px;background:linear-gradient(160deg,#1d1d1d,#3c3c3c 70%,#cfcfcf 71%,#e4e4e4);border-radius:8px;opacity:.85}
.hero-shapes{left:0;top:0}
.brand{left:173px;top:40px;display:flex;align-items:center;gap:18px}
.brand-square{width:81px;height:70px;background:var(--white)}
.brand-name{font-family:var(--font-light);font-size:24px;color:var(--white);letter-spacing:1px}
.nav{top:26px;left:727px;display:flex;gap:40px;font-family:var(--font-light);font-size:17px;color:var(--white)}
.login{left:938px;top:24px;width:88px;height:30px;border:2px solid var(--white);color:var(--white);font-family:var(--font-light);font-size:17px;display:flex;align-items:center;justify-content:center;gap:8px}
.call{left:820px;top:86px;display:flex;gap:10px;align-items:center;color:var(--white);font-family:var(--font-light);font-size:18px}
.hero-title{right:172px;top:352px;text-align:right;font-family:var(--font-bold);font-weight:700;color:#1e1e1e;line-height:1}
.hero-title .l1{font-size:48px}
.hero-title .l2{font-size:60px}
.read-more{left:915px;top:472px;width:111px;height:41px;border:3px solid var(--red);color:var(--red);font-family:var(--font-bold);font-weight:600;font-size:15px;display:flex;align-items:center;justify-content:center}
.dots{left:557px;top:675px;display:flex;gap:10px}
.dots span{width:14px;height:14px;background:var(--white)}
.dots .on{background:transparent;border:2px solid var(--red)}
.badge{top:790px;width:203px;height:119px;border:4px solid var(--frame);display:flex;align-items:center;justify-content:center}
.badge i{display:block;width:120px;height:40px;background:#ececec;border-radius:4px}
.section-title{left:0;width:1200px;text-align:center;font-family:var(--font-light);font-size:38px;color:#222;line-height:45px}
.section-title b{font-family:var(--font-bold);font-weight:700;color:var(--red)}
.sub{left:0;width:1200px;text-align:center;font-size:13px;color:#444}
.device{top:1168px;width:203px;height:237px;border:8px solid var(--frame);text-align:center}
.device .pic{margin:18px auto 0;width:130px;height:135px;border-radius:6px;background:linear-gradient(160deg,#2c4d7a,#9bb3cc 60%,#dcdcdc)}
.device .label{margin-top:18px;font-family:var(--font-light);font-size:19px;color:#444}
.how-bg{left:0;top:1455px}
.how-title{color:var(--white)}
.how-sub{color:var(--white)}
.step{top:1697px;width:268px;height:256px;background:#e4e4e4;padding:14px}
.step-inner{width:100%;height:100%;background:var(--white);border:2px solid var(--red);text-align:center;padding-top:28px}
.step-art{margin:0 auto;width:124px;height:108px;background:linear-gradient(135deg,#f3f3f3,#e6dcdd);border-radius:4px}
.step-title{margin-top:14px;font-family:var(--font-light);font-size:19px;color:#222}
.step-sub{margin-top:4px;font-size:11px;color:#555}
.about-title{left:172px;top:2258px;font-family:var(--font-light);font-size:38px;color:#222}
.about-title b{font-family:var(--font-bold);font-weight:700;color:var(--red)}
.about-text{left:172px;top:2318px;width:400px;font-size:11px;line-height:22.4px;color:#444}
.about-frame{left:733px;top:2260px;width:324px;height:280px;border:7px solid var(--red)}
.about-photo{left:681px;top:2228px;width:347px;height:284px;background:linear-gradient(135deg,#5a3a24,#7a4e30 50%,#d9d9d9 51%,#3a2a20)}
.footer-bg{left:0;top:2620px}
.contact-head{left:172px;top:2690px;font-family:var(--font-bold);font-weight:600;font-size:15px;color:var(--white)}
.contact{left:172px;top:2725px;font-size:11px;color:var(--white);line-height:22px}
.contact div{display:flex;gap:12px;align-items:center}
.contact .indent{padding-left:20px}
.follow{left:916px;top:2754px;display:flex;gap:8px;align-items:center;font-size:13px;color:var(--white)}
.follow i{display:block;width:16px;height:16px;border:2px solid var(--white)}
.links{right:173px;top:2792px;display:flex;gap:22px;font-size:12.5px;color:var(--white)}
.bottom-bar{left:0;top:2832px;width:1200px;height:64px;background:var(--red-deep)}
.foot-brand{left:170px;top:2843px;display:flex;gap:12px;align-items:center}
.foot-brand i{display:block;width:46px;height:42px;background:var(--white)}
.foot-brand span{font-family:var(--font-light);font-size:15px;color:var(--white)}
.copy{right:173px;top:2860px;font-size:11px;color:var(--white)}
</style>
</head>
<body>

<header>
  <div class="abs hero-photo" role="img" aria-label="Photo of an open laptop and a cup of tea on a wooden desk"></div>
  <div class="abs laptop-area" role="img" aria-label="Open laptop on desk"></div>
  <svg class="abs hero-shapes" width="1200" height="240" viewBox="0 0 1200 240">
    <polygon points="0,0 1200,0 1200,190 1020,155 455,100 233,197 0,101" fill="#c30a1c"/>
    <polygon points="700,0 1200,0 1200,190 1020,155 880,110" fill="#7d0510" opacity=".55"/>
  </svg>
  <div class="abs brand"><span class="brand-square"></span><span class="brand-name">PEBBLE7DOCK</span></div>
  <nav class="abs nav"><span>Sell</span><span>Track</span><span>Join</span></nav>
  <div class="abs login">
    <svg width="10" height="13" viewBox="0 0 10 13"><circle cx="5" cy="3.5" r="3" fill="#fff"/><path d="M0 13 Q0 7 5 7 Q10 7 10 13Z" fill="#fff"/></svg>Login</div>
  <div class="abs call">
    <svg width="15" height="15" viewBox="0 0 24 24"><path d="M6.6 10.8a15 15 0 0 0 6.6 6.6l2.2-2.2c.3-.3.7-.4 1-.2 1.1.4 2.3.6 3.6.6.6 0 1 .4 1 1V20c0 .6-.4 1-1 1A17 17 0 0 1 3 4c0-.6.4-1 1-1h3.5c.6 0 1 .4 1 1 0 1.3.2 2.5.6 3.6.1.3 0 .7-.2 1z" fill="#fff"/></svg>
    Call Us: 555-201-4477</div>
  <h1 class="abs hero-title"><span class="l1">Welcome to</span><br><span class="l2">Pebble7dock</span></h1>
  <div class="abs read-more">Read More</div>
  <div class="abs dots"><span></span><span></span><span class="on"></span><span></span></div>
</header>

<section class="trust">
  <div class="abs badge" style="left:172px"><i></i></div>
  <div class="abs badge" style="left:390px"><i></i></div>
  <div class="abs badge" style="left:607px"><i></i></div>
  <div class="abs badge" style="left:825px"><i></i></div>
</section>

<section class="devices">
  <h2 class="abs section-title" style="top:1012px">Select Your Device to<br>Receive an <b>Instant Quote</b></h2>
  <p class="abs sub" style="top:1116px">Nequeporrouisquam esti dolorem iseque porro</p>
  <div class="abs device" style="left:172px"><div class="pic" role="img" aria-label="Orvex phone"></div><div class="label">Orvex Phone</div></div>
  <div class="abs device" style="left:390px"><div class="pic" role="img" aria-label="Orvex tablets"></div><div class="label">Orvex Tab</div></div>
  <div class="abs device" style="left:607px"><div class="pic" role="img" aria-label="Orvex laptop"></div><div class="label">Orvex Book</div></div>
  <div class="abs device" style="left:825px"><div class="pic" role="img" aria-label="Orvex desktop computer"></div><div class="label">Orvex Desk</div></div>
</section>

<section class="how">
  <svg class="abs how-bg" width="1200" height="690" viewBox="0 0 1200 690" role="img" aria-label="Red toned photo of a laptop on a desk">
    <defs><linearGradient id="howGrad" x1="0" y1="0" x2="1" y2="1"><stop offset="0" stop-color="#d3101f"/><stop offset=".6" stop-color="#b70818"/><stop offset="1" stop-color="#8e0612"/></linearGradient></defs>
    <polygon points="0,20 604,81 1200,5 1200,680 604,625 0,685" fill="url(#howGrad)"/>
  </svg>
  <h2 class="abs section-title how-title" style="top:1597px">How It Works</h2>
  <p class="abs sub how-sub" style="top:1653px">Nequeporrouisquam esti dolorem iseque porro</p>

  <div class="abs step" style="left:172px"><div class="step-inner">
    <div class="step-art" role="img" aria-label="Step one illustration: number one with a discount offer icon"></div>
    <div class="step-title">Get An Offer</div><div class="step-sub">Less than a minute</div></div></div>

  <div class="abs step" style="left:465px"><div class="step-inner">
    <div class="step-art" role="img" aria-label="Step two illustration: number two with a shipping box icon"></div>
    <div class="step-title">Ship It Free</div><div class="step-sub">We provide a pre-paid shipping label</div></div></div>

  <div class="abs step" style="left:758px"><div class="step-inner">
    <div class="step-art" role="img" aria-label="Step three illustration: number three with a hand receiving money icon"></div>
    <div class="step-title">Get Paid Fast</div><div class="step-sub">Online wallet, check or bank transfer</div></div></div>
</section>

<section class="about">
  <div class="abs about-frame"></div>
  <div class="abs about-photo" role="img" aria-label="Top view of a wooden desk with keyboard, laptop, tablets and glasses"></div>
  <h2 class="abs about-title">About <b>Pebble7dock</b></h2>
  <p class="abs about-text">Lorem ipsum dolor sit amet, consectetur adipiscing elit, sed do eiusmod te orem ipsum dolor sit amet, consectetur adipiscing elit, sed do eiusmod te mpor incididunt ut labore et dolore magna aliqua. Ut enim ad minim ve niam, quis nostrud exercitation ullamco laboris nisi ut aliquip ex ea como consequat. Duis aute irure dolor in reprehenderit in voluptate velmpor inc didunt ut labore et dolore magna aliqua. Ut enim ad minim veniam, quis no strud exercitation ullamco laboris nisi ut aliquip ex ea commodo conseuat uis aute irure dolor in reprehenderit in voluptate vel</p>
</section>

<footer>
  <svg class="abs footer-bg" width="1200" height="276" viewBox="0 0 1200 276">
    <polygon points="0,108 233,15 400,110 604,12 1200,100 1200,276 0,276" fill="#c30a1c"/>
    <polygon points="604,12 1200,100 1200,276 560,276 430,140" fill="#8e0612" opacity=".6"/>
  </svg>
  <div class="abs contact-head">Get In Touch:</div>
  <div class="abs contact">
    <div><svg width="8" height="11" viewBox="0 0 8 11"><path d="M4 0a4 4 0 0 1 4 4c0 3-4 7-4 7S0 7 0 4a4 4 0 0 1 4-4z" fill="#fff"/><circle cx="4" cy="4" r="1.5" fill="#c30a1c"/></svg>Pebble7dock</div>
    <div class="indent">48 Linden Row</div>
    <div class="indent">Clearbrook, NY, 10000</div>
    <div><svg width="9" height="9" viewBox="0 0 24 24"><path d="M6.6 10.8a15 15 0 0 0 6.6 6.6l2.2-2.2c.3-.3.7-.4 1-.2 1.1.4 2.3.6 3.6.6.6 0 1 .4 1 1V20c0 .6-.4 1-1 1A17 17 0 0 1 3 4c0-.6.4-1 1-1h3.5c.6 0 1 .4 1 1 0 1.3.2 2.5.6 3.6.1.3 0 .7-.2 1z" fill="#fff"/></svg>555-201-4477</div>
  </div>
  <div class="abs follow">Follow Us <i></i><i></i></div>
  <nav class="abs links"><span>About Us</span><span>FAQs</span><span>Terms of Service</span><span>Privacy Policy</span><span>Contact Us</span></nav>
  <div class="abs bottom-bar"></div>
  <div class="abs foot-brand"><i></i><span>PEBBLE7DOCK</span></div>
  <div class="abs copy">© 2019 — All rights reserved. Pebble7dock</div>
</footer>

</body>
</html>
```